Yacht Management in Miami & Ft Lauderdale (2019Q2)

I’m looking for a flyer to leave places for people to get information about my company and what services we offer.
We offer monthly management plans to ensure the vessel is ready to go at a moments notice. This can be as simple as washing once a week, or as involved as washing, waxing, detailing, provisioning, and crew services.
We also offer bespoke customizations; stereos, on board WiFi, and engineering.

Target Market(s)

Yacht and boat owners.

Font styles to use
Sans Serif

Colors
87d0c7
85cae6
85acd3
cedeed
cee9f5
cfeae6
0455a3

Requirements
Must have
• Must have simple attention grabbing, without being obnoxious.
• Prefer a 3in x 5in post card size. other size may be an option.
• Must be front and back.
Nice to have
• Languages: English, Spanish, Russian
• USA flag logo
Should not have
• Should not have a lot of text. Icons and photos are great.

```html
<!DOCTYPE html>
<html lang="en">
<head>
<meta charset="utf-8">
<title>Harbor Sages – Flyer Front and Back</title>
<link href="https://fonts.googleapis.com/css2?family=Montserrat:wght@600;700&family=Questrial&display=swap" rel="stylesheet">
<style>
  :root{
    --stage:#6d6d6d;
    --paper:#ffffff;
    --ink:#1f1f1f;
    --band:#242424;
    --panel:#3b3b3b;
    --bar:#4a4a4a;
    --hex-dark:#333333;
    --hex-mid:#424242;
    --red:#ee2a1a;
    --yellow:#f4e300;
    --muted:#e6e6e6;
  }
  *{box-sizing:border-box;margin:0;padding:0}
  html,body{width:1200px;height:1200px;overflow:hidden}
  body{background:var(--stage);position:relative;font-family:"Questrial",sans-serif;color:var(--ink)}
  .flyer{position:absolute;top:206px;width:558px;height:788px;background:var(--paper);overflow:hidden}
  .flyer--front{left:27px}
  .flyer--back{left:614px;height:786px}

  /* brand name */
  .brand{position:absolute;font-family:"Montserrat",sans-serif;font-weight:700;color:var(--ink);text-transform:uppercase;text-align:center;line-height:1.05}
  .flyer--front .brand{left:414px;top:70px;width:122px;font-size:24px}
  .flyer--back .brand{left:440px;top:232px;width:100px;font-size:20px}

  /* front */
  .hex-gallery{position:absolute;left:0;top:0}
  .headline{position:absolute;left:0;top:475px;width:558px;height:93px;background:var(--band);color:#fff;
    font-weight:400;font-size:28px;line-height:37px;padding:10px 0 0 28px;text-transform:uppercase;white-space:nowrap}
  .intro{position:absolute;left:27px;top:586px;width:500px;font-size:14.4px;line-height:18.5px;text-align:justify}
  .intro p+p{margin-top:14px}
  .front-footer{position:absolute;left:0;top:736px;width:558px;height:52px;background:var(--red)}
  .phone-pill{position:absolute;left:25px;top:705px;width:224px;height:100px;background:var(--band);border-radius:60px 60px 0 0;color:#fff;text-align:center}
  .phone-pill svg{margin-top:9px}
  .phone-pill .number{font-size:29px;letter-spacing:1px;margin-top:2px}
  .front-web{position:absolute;left:270px;top:751px;color:#fff;font-size:17px;display:flex;align-items:center;gap:10px;letter-spacing:.3px;white-space:nowrap}
  .front-divider{position:absolute;left:442px;top:746px;width:1px;height:34px;background:rgba(255,255,255,.8)}
  .follow{position:absolute;left:458px;top:744px;color:#fff;font-size:12px;font-family:"Montserrat",sans-serif;font-weight:600}
  .follow .dots{display:flex;gap:8px;margin:4px 0 0 10px}
  .follow .dots span{width:13px;height:13px;border-radius:50%;background:#fff}

  /* back */
  .interior-photo{position:absolute;left:0;top:0}
  .tagline{position:absolute;left:0;top:350px;width:558px;height:42px;background:var(--bar);color:#fff;font-size:19px;padding:7px 0 0 26px;border-left:3px solid var(--red);letter-spacing:.2px}
  .services{position:absolute;left:0;top:400px;width:558px;height:276px;background:var(--panel);color:#fff}
  .col{position:absolute;top:12px}
  .col--main{left:26px;width:190px}
  .col--extra{left:250px;width:288px}
  .col-divider{position:absolute;left:227px;top:20px;width:0;height:242px;border-left:1px dashed rgba(255,255,255,.55)}
  .col h2{font-family:"Montserrat",sans-serif;font-weight:700;font-size:14px;line-height:18px;margin-bottom:10px}
  .service h3{font-family:"Montserrat",sans-serif;font-weight:700;font-size:14px;color:var(--yellow);display:flex;align-items:center;gap:7px;margin-bottom:6px}
  .service p{font-size:9.8px;line-height:13px;color:var(--muted);text-align:justify}
  .col--main .service{margin-bottom:16px}
  .col--extra .service{margin-bottom:10px}
  .col--extra .service p{font-size:8.6px;line-height:11.3px}
  .red-rule{position:absolute;left:0;top:679px;width:558px;height:8px;background:var(--red)}
  .back-phone{position:absolute;left:26px;top:714px;display:flex;align-items:center;gap:18px;font-size:35px;letter-spacing:1.5px;color:var(--ink);white-space:nowrap}
  .back-divider{position:absolute;left:322px;top:706px;width:2px;height:64px;background:var(--red)}
  .back-web{position:absolute;left:340px;top:724px;display:flex;align-items:center;gap:12px;font-size:21px;letter-spacing:.5px;white-space:nowrap}
</style>
</head>
<body>

<section class="flyer flyer--front">
  <svg class="hex-gallery" width="558" height="460" viewBox="0 0 558 460" role="img" aria-label="Photo of a motor yacht moored at night with green underwater lights, shown through a honeycomb of hexagons">
    <defs>
      <linearGradient id="nightHarbor" gradientUnits="userSpaceOnUse" x1="0" y1="52" x2="0" y2="440">
        <stop offset="0" stop-color="#5c2232"/>
        <stop offset=".35" stop-color="#2e3448"/>
        <stop offset=".62" stop-color="#1e2622"/>
        <stop offset="1" stop-color="#3f8a2e"/>
      </linearGradient>
    </defs>
    <g fill="url(#nightHarbor)" stroke="#fff" stroke-width="1">
      <polygon points="67,52 134,91 134,168 67,207 0,168 0,91"/>
      <polygon points="201,52 268,91 268,168 201,207 134,168 134,91"/>
      <polygon points="335,52 402,91 402,168 335,207 268,168 268,91"/>
      <polygon points="0,168 67,207 67,284 0,323 -67,284 -67,207"/>
      <polygon points="134,168 201,207 201,284 134,323 67,284 67,207"/>
      <polygon points="268,168 335,207 335,284 268,323 201,284 201,207"/>
      <polygon points="402,168 469,207 469,284 402,323 335,284 335,207"/>
      <polygon points="67,284 134,323 134,400 67,439 0,400 0,323"/>
      <polygon points="201,284 268,323 268,400 201,439 134,400 134,323"/>
      <polygon points="335,284 402,323 402,400 335,439 268,400 268,323"/>
    </g>
    <polygon points="536,168 603,207 603,284 536,323 469,284 469,207" fill="var(--hex-mid)"/>
    <polygon points="469,284 536,323 536,400 469,439 402,400 402,323" fill="var(--hex-dark)"/>
  </svg>

  <div class="brand">Harbor<br>Sages</div>

  <h1 class="headline">Harbor Sages are here to refit<br>and update your yacht</h1>

  <div class="intro">
    <p>We offer monthly management plans to ensure the vessel is ready to go at a moments notice. This can be as simple as washing once a week, or as involved as washing, waxing, detailing, provisioning, and crew services.</p>
    <p>We also offer bespoke customizations; stereos, on board WiFi, and engineering.</p>
  </div>

  <div class="front-footer"></div>
  <div class="phone-pill">
    <svg width="30" height="30" viewBox="0 0 30 30" aria-hidden="true">
      <circle cx="15" cy="15" r="15" fill="#fff"/>
      <path d="M10 8c1-1 2 0 3 2s0 2-1 3c1 2 3 4 5 5 1-1 2-2 3-1s3 2 2 3-3 2-5 1c-4-2-7-5-8-9-1-2 0-3 1-4z" fill="var(--band)"/>
    </svg>
    <div class="number">555 014 2271</div>
  </div>
  <div class="front-web">
    <svg width="20" height="20" viewBox="0 0 24 24" fill="none" stroke="#fff" stroke-width="1.6" aria-hidden="true">
      <circle cx="12" cy="12" r="10"/><ellipse cx="12" cy="12" rx="4.5" ry="10"/><path d="M2 12h20M4 6.5h16M4 17.5h16"/>
    </svg>
    <span>harborsages.us</span>
  </div>
  <div class="front-divider"></div>
  <div class="follow">Follow Us:<div class="dots"><span></span><span></span></div></div>
</section>

<section class="flyer flyer--back">
  <svg class="interior-photo" width="558" height="350" viewBox="0 0 558 350" role="img" aria-label="Photo of a luxury yacht salon with cream sofas, wood trim, a wall screen and wide windows">
    <defs>
      <linearGradient id="salon" x1="0" y1="0" x2="0" y2="1">
        <stop offset="0" stop-color="#6b4a36"/>
        <stop offset=".3" stop-color="#3f6fb8"/>
        <stop offset=".6" stop-color="#cdbfa8"/>
        <stop offset="1" stop-color="#8a6a4c"/>
      </linearGradient>
    </defs>
    <polygon points="0,198 250,336 236,346 0,222" fill="#3a3a3a"/>
    <polygon points="0,0 524,0 524,170 244,331 0,196" fill="url(#salon)"/>
  </svg>

  <div class="brand">Harbor<br>Sages</div>

  <div class="tagline">We offer bespoke services to compliment any system.</div>

  <div class="services">
    <div class="col col--main">
      <h2>Fair &amp; Friendly Yacht<br>Service</h2>
      <div class="service">
        <h3><svg width="13" height="11" viewBox="0 0 13 11" aria-hidden="true"><path d="M1 6l4 4 7-9" fill="none" stroke="var(--red)" stroke-width="1.6"/></svg>AUDIO:</h3>
        <p>We perform most projects in-house, from design to installation.</p>
      </div>
      <div class="service">
        <h3><svg width="13" height="11" viewBox="0 0 13 11" aria-hidden="true"><path d="M1 6l4 4 7-9" fill="none" stroke="var(--red)" stroke-width="1.6"/></svg>VISUAL:</h3>
        <p>Tv’s on custom lifts and fold outs. StreamBox, Orbit Media Servers and more.</p>
      </div>
      <div class="service">
        <h3><svg width="13" height="11" viewBox="0 0 13 11" aria-hidden="true"><path d="M1 6l4 4 7-9" fill="none" stroke="var(--red)" stroke-width="1.6"/></svg>INTERNET:</h3>
        <p>Domestic Connectivity (cellular) Marina Connectivity (Wi-Fi WAN) On board Wi-Fi (2.4GHz &amp; 5Ghz)</p>
      </div>
    </div>
    <div class="col-divider"></div>
    <div class="col col--extra">
      <h2>Additional Services</h2>
      <div class="service">
        <h3><svg width="13" height="11" viewBox="0 0 13 11" aria-hidden="true"><path d="M1 6l4 4 7-9" fill="none" stroke="var(--red)" stroke-width="1.6"/></svg>VOYAGES:</h3>
        <p>Taking your vessel from Miami, Fort Lauderdale, or Palm Beach locally or to the Bahamas, Ocean Reef, the Keys, or Cuba. What else did you buy your boat for?</p>
      </div>
      <div class="service">
        <h3><svg width="13" height="11" viewBox="0 0 13 11" aria-hidden="true"><path d="M1 6l4 4 7-9" fill="none" stroke="var(--red)" stroke-width="1.6"/></svg>PACKAGE SALES:</h3>
        <p>Are you a Do-It-Yourself person? We offer packages with most everything you’ll need to install an A/C pump, stereo, TabPro wall control, or Sonara. We can even help you out over the phone if you hit a roadblock.</p>
      </div>
      <div class="service">
        <h3><svg width="13" height="11" viewBox="0 0 13 11" aria-hidden="true"><path d="M1 6l4 4 7-9" fill="none" stroke="var(--red)" stroke-width="1.6"/></svg>TROUBLESHOOTING:</h3>
        <p>When your head is up against the wall, that’s where we really shine. With experience on every major brand and many more bespoke brands, we are able to diagnose most issues. Even if we don’t have an exact answer, we know the right people to call to get the right answer.</p>
      </div>
    </div>
  </div>

  <div class="red-rule"></div>
  <div class="back-phone">
    <svg width="32" height="32" viewBox="0 0 32 32" aria-hidden="true">
      <circle cx="16" cy="16" r="14" fill="none" stroke="var(--red)" stroke-width="2.4"/>
      <path d="M11 9c1-1 2 0 3 2s0 2-1 3c1 2 3 4 5 5 1-1 2-2 3-1s3 2 2 3-3 2-5 1c-4-2-7-5-8-9-1-2 0-3 1-4z" fill="var(--red)"/>
    </svg>
    <span>555 014 2271</span>
  </div>
  <div class="back-divider"></div>
  <div class="back-web">
    <svg width="20" height="20" viewBox="0 0 24 24" fill="none" stroke="var(--red)" stroke-width="1.6" aria-hidden="true">
      <circle cx="12" cy="12" r="10"/><ellipse cx="12" cy="12" rx="4.5" ry="10"/><path d="M2 12h20M4 6.5h16M4 17.5h16"/>
    </svg>
    <span>harborsages.us</span>
  </div>
</section>

</body>
</html>
```